Radiant Harbor Holdings business card

We are a real estate advisory and investment company. We are specialized in assisting high networth individuals to invest in real estate overseas. We deliver a very personalized service, anticipating all the potential challenges an investor can face, and making it easy and safe for them. We also co-invest with our clients, assuring them that each project will be looked after as it is our own, and at the same time giving them the extra booth on confidence to invest.

We need a business card design. The business card must have a very premium, high-end look, reflecting principles like "commitment", "trust" and "timeless (but contemporary)". We look for long term relationships with our clients, and we grow with their referrals. We are all about conquering the confidence of the clients by always delivering above the expectations performance.

Target Market(s)

High net worth individuals.

Industry/Entity Type

Real Estate

Contact Information for Business Card

Please consider places on the business card for:

Name
Function (bellow name in smaller size text)

Mobile phone
E-mail
Skype ID
WeChat ID

Adress (3 lines)

Also include the following locations references:
PORTUGAL * DUBAI * HONG KONG

Website: www.rhholdings.example

Requirements
Must have
• Company Logo

```html
<!DOCTYPE html>
<html lang="en">
<head>
<meta charset="utf-8">
<title>Radiant Harbor Holdings — Business Card</title>
<link href="https://fonts.googleapis.com/css2?family=Cinzel:wght@500&family=Montserrat:wght@400;500;700&display=swap" rel="stylesheet">
<style>
  :root {
    --brand-blue: #29abe2;
    --ink-grey: #6d6e71;
    --paper: #ffffff;
    --backdrop: #eceef0;
    --rule-grey: #9a9b9e;
  }
  * { box-sizing: border-box; margin: 0; padding: 0; }
  html, body { width: 1200px; height: 900px; overflow: hidden; }
  body {
    background: var(--backdrop);
    position: relative;
    font-family: "Montserrat", Arial, sans-serif;
  }
  .card {
    position: absolute;
    width: 600px;
    height: 343px;
    border-radius: 22px;
    box-shadow: 0 10px 28px rgba(0,0,0,0.14);
    overflow: hidden;
  }

  /* Back side */
  .card-back {
    left: 70px; top: 90px;
    background: var(--brand-blue);
    color: var(--paper);
  }
  .back-name {
    position: absolute;
    left: 0; right: 0; top: 92px;
    text-align: center;
    font-family: "Cinzel", Georgia, serif;
    font-weight: 500;
    font-size: 34px;
    letter-spacing: 2px;
    color: var(--paper);
  }
  .back-website {
    position: absolute;
    left: 0; right: 0; top: 196px;
    text-align: center;
    font-size: 17px;
    letter-spacing: 0.5px;
  }
  .back-locations {
    position: absolute;
    left: 0; right: 0; top: 266px;
    text-align: center;
    font-size: 17px;
    font-weight: 700;
    letter-spacing: 1px;
  }

  /* Front side */
  .card-front {
    left: 530px; top: 467px;
    background: var(--paper);
  }
  .brand {
    position: absolute;
    left: 30px; top: 150px;
    width: 290px;
  }
  .brand-name {
    font-family: "Cinzel", Georgia, serif;
    font-weight: 500;
    font-size: 26px;
    line-height: 1.2;
    letter-spacing: 1px;
    color: var(--brand-blue);
  }
  .divider {
    position: absolute;
    left: 338px; top: 46px;
    width: 1px; height: 200px;
    background: var(--brand-blue);
  }
  .contact {
    position: absolute;
    left: 360px; top: 46px;
    color: var(--ink-grey);
    font-size: 15px;
    line-height: 1.25;
  }
  .person-name {
    font-family: "Cinzel", Georgia, serif;
    font-weight: 500;
    font-size: 20px;
    color: var(--brand-blue);
    letter-spacing: 0.5px;
  }
  .person-function { font-size: 14px; margin-bottom: 10px; }
  .address { padding-left: 22px; margin-bottom: 10px; }
  .contact-list { list-style: none; }
  .contact-list li { display: flex; align-items: center; gap: 8px; }
  .contact-list svg { width: 13px; height: 13px; flex: none; }
  .accent { color: var(--brand-blue); }
</style>
</head>
<body>
  <section class="card card-back" aria-label="Card back">
    <p class="back-name">Radiant Harbor Holdings</p>
    <p class="back-website">www.rhholdings.example</p>
    <p class="back-locations">PORTUGAL - DUBAI - HONG KONG</p>
  </section>

  <section class="card card-front" aria-label="Card front">
    <div class="brand">
      <p class="brand-name">Radiant Harbor Holdings</p>
    </div>
    <div class="divider"></div>
    <div class="contact">
      <p class="person-name">MARCUS ELLERY</p>
      <p class="person-function">Function</p>
      <p class="address">PO Box 4870<br>Harbor Court<br>NSW 2011</p>
      <ul class="contact-list">
        <li>
          <svg viewBox="0 0 16 16" aria-hidden="true"><path d="M4 1.5l2.5 3-1.5 1.8c.8 1.8 2.2 3.2 4 4l1.8-1.5 3 2.5-1.6 2.2C7 13.2 2.8 9 1.8 3.1z" fill="var(--brand-blue)"/></svg>
          +330 5550-0142
        </li>
        <li>
          <svg viewBox="0 0 16 16" aria-hidden="true"><rect x="1.5" y="3.5" width="13" height="9" fill="none" stroke="var(--brand-blue)" stroke-width="1.6"/><path d="M1.5 3.5L8 9l6.5-5.5" fill="none" stroke="var(--brand-blue)" stroke-width="1.6"/></svg>
          info@rhholdings.example
        </li>
        <li>
          <svg viewBox="0 0 16 16" aria-hidden="true"><circle cx="8" cy="8" r="6.5" fill="none" stroke="var(--brand-blue)" stroke-width="1.4"/><ellipse cx="8" cy="8" rx="2.8" ry="6.5" fill="none" stroke="var(--brand-blue)" stroke-width="1.2"/><path d="M1.5 8h13" stroke="var(--brand-blue)" stroke-width="1.2"/></svg>
          <span>www.<span class="accent">rhholdings</span>.example</span>
        </li>
      </ul>
    </div>
  </section>
</body>
</html>
```